Velmora Handel Stationary
Simple
Jonas Brückler
Co-Founder
Velmora Handel UG
Lindenkamp 12
48213 Ostenbrück am Hain
Germany
jonas.brueckler@velmora-handel.example
www.velmora-handel.example
Please use the some font as in the logo and work out a proposal based on the red and yellow logo in the uploaded rar file. Whether or not you use the globe in the back (you will see in the rar file) is up to you. The corporate slogan 'Your gateway to infinite opportunities' can be integrated but it's not a must.
Corporate Logo (with or without slogan, up to you)
Please refer to the logos. Ideally work sth out from the colorful version (red and yellow) with or without the globe in the back. You will see when looking at the file.

```html
<!DOCTYPE html>
<html lang="de">
<head>
<meta charset="utf-8">
<title>Velmora Handel Stationary</title>
<link href="https://fonts.googleapis.com/css2?family=Arimo:wght@400;700&display=swap" rel="stylesheet">
<style>
  :root{
    --red:#d4161c;
    --deep-red:#8e0f18;
    --maroon:#5e0a12;
    --orange:#f47a12;
    --yellow:#ffc21a;
    --ink:#3a3a3a;
    --paper:#ffffff;
    --edge:#c9c9c9;
  }
  *{margin:0;padding:0;box-sizing:border-box}
  html,body{width:1200px;height:742px;overflow:hidden;background:#fff}
  body{position:relative;font-family:"Arimo",Arial,sans-serif;color:var(--ink)}
  .piece{position:absolute;overflow:hidden;border:1px solid var(--edge);box-shadow:1px 1px 3px rgba(0,0,0,.18)}
  .piece svg.swoosh{position:absolute;inset:0;width:100%;height:100%}
  .brand{position:absolute;display:flex;align-items:center;gap:8px;font-weight:700;color:var(--red);letter-spacing:.04em;white-space:nowrap}
  .brand .dot{border-radius:50%;background:var(--red);flex:none}
  .brand.on-dark{color:#fff}
  .brand.on-dark .dot{background:var(--yellow)}
  .label{color:var(--red)}

  /* Letterhead */
  .letterhead{left:48px;top:19px;width:523px;height:701px;background:var(--paper)}
  .letterhead .brand{left:26px;top:60px;font-size:22px}
  .letterhead .brand .dot{width:30px;height:30px}
  .letterhead .footer{position:absolute;left:26px;bottom:22px;font-size:9.5px;line-height:14px;white-space:nowrap}

  /* Business card front */
  .card-front{left:598px;top:52px;width:214px;height:126px;background:var(--paper)}
  .card-front .brand{left:10px;top:12px;font-size:9.5px;gap:4px}
  .card-front .brand .dot{width:13px;height:13px}
  .card-front .person{position:absolute;left:138px;top:12px;font-size:5.5px;line-height:8px;white-space:nowrap}
  .card-front .person strong{color:var(--red)}
  .card-front .details{position:absolute;left:10px;top:58px;font-size:5.5px;line-height:8px;white-space:nowrap}

  /* Card backs */
  .card-back{display:flex;align-items:center;justify-content:center}
  .card-back .brand{position:static;font-size:14px}
  .card-back .brand .dot{width:20px;height:20px}
  .card-black{left:898px;top:91px;width:208px;height:132px;background:#000}
  .card-grey{left:617px;top:216px;width:201px;height:108px;background:linear-gradient(135deg,#9a9a9a,#7c7c7c)}
  .card-red{left:917px;top:245px;width:211px;height:110px;background:linear-gradient(90deg,var(--red),var(--deep-red))}

  /* Envelope */
  .envelope{left:576px;top:384px;width:600px;height:336px;background:var(--paper)}
  .envelope .flap{position:absolute;left:0;top:0;width:100%;height:72px;background:linear-gradient(90deg,var(--red),var(--deep-red) 80%,var(--maroon));display:flex;align-items:center;justify-content:center}
  .envelope .flap .brand{position:static;font-size:14px}
  .envelope .flap .brand .dot{width:22px;height:22px}
  .envelope .brand.sender{left:32px;top:110px;font-size:16px}
  .envelope .brand.sender .dot{width:24px;height:24px}
  .envelope .sender-address{position:absolute;left:32px;top:158px;font-size:9px;line-height:12px;white-space:nowrap}
</style>
</head>
<body>

<section class="piece letterhead">
  <svg class="swoosh" viewBox="0 0 523 701" preserveAspectRatio="none" aria-hidden="true">
    <defs>
      <linearGradient id="lh-band" x1="0" y1="0" x2="1" y2="0">
        <stop offset="0" stop-color="#e0261a"/>
        <stop offset=".55" stop-color="#a8121a"/>
        <stop offset="1" stop-color="#5e0a12"/>
      </linearGradient>
    </defs>
    <path d="M402 0 Q585 330 448 701 L523 701 L523 0 Z" fill="url(#lh-band)"/>
    <path d="M402 0 Q585 330 448 701" fill="none" stroke="#f47a12" stroke-width="16"/>
    <path d="M398 0 Q578 330 442 701" fill="none" stroke="#ffc21a" stroke-width="6"/>
  </svg>
  <div class="brand"><span class="dot"></span>VELMORA HANDEL</div>
  <div class="footer">
    Velmora Handel UG, Lindenkamp 12, 48213 Ostenbrück am Hain, Germany<br>
    <span class="label">Phone:</span> +49 3601 4820 - 17 | <span class="label">Cell:</span> +49 152 40 71 2296<br>
    <span class="label">Email:</span> jonas.brueckler@velmora-handel.example | <span class="label">www.velmora-handel.example</span>
  </div>
</section>

<section class="piece card-front">
  <div class="brand"><span class="dot"></span>VELMORA HANDEL</div>
  <div class="person"><strong>Jonas Brückler</strong><br>Co-Founder</div>
  <div class="details">
    Velmora Handel UG, Lindenkamp 12<br>
    48213 Ostenbrück am Hain, Germany<br>
    <span class="label">Phone:</span> +49 3601 4820 - 17<br>
    <span class="label">Cell:</span> +49 152 40 71 2296<br>
    jonas.brueckler@velmora-handel.example<br>
    www.velmora-handel.example
  </div>
</section>

<section class="piece card-back card-black">
  <div class="brand on-dark"><span class="dot"></span>VELMORA</div>
</section>

<section class="piece card-back card-grey">
  <div class="brand on-dark"><span class="dot"></span>VELMORA</div>
</section>

<section class="piece card-back card-red">
  <div class="brand on-dark"><span class="dot"></span>VELMORA</div>
</section>

<section class="piece envelope">
  <svg class="swoosh" viewBox="0 0 600 336" preserveAspectRatio="none" aria-hidden="true">
    <defs>
      <linearGradient id="env-band" x1="0" y1="0" x2="1" y2="0">
        <stop offset="0" stop-color="#e0261a"/>
        <stop offset=".6" stop-color="#a8121a"/>
        <stop offset="1" stop-color="#5e0a12"/>
      </linearGradient>
    </defs>
    <path d="M430 72 Q590 190 470 336 L600 336 L600 72 Z" fill="url(#env-band)"/>
    <path d="M430 72 Q590 190 470 336" fill="none" stroke="#f47a12" stroke-width="14"/>
    <path d="M426 72 Q584 190 464 336" fill="none" stroke="#ffc21a" stroke-width="5"/>
  </svg>
  <div class="flap">
    <div class="brand on-dark"><span class="dot"></span>VELMORA</div>
  </div>
  <div class="brand sender"><span class="dot"></span>VELMORA HANDEL</div>
  <div class="sender-address">
    Velmora Handel UG, Lindenkamp 12<br>
    48213 Ostenbrück am Hain, Germany
  </div>
</section>

</body>
</html>
```